Gym Poster to advertise for our chiropractic business

We are needing a poster for a gym. They are a weight training gym, Copper Ridge Gym. The poster will be 4 ft by 8 ft. This poster will be used for advertising purposes.
Target Market(s)
Athletes, 25 to 45,Men and Women,
Industry/Entity Type
Advertising
Font styles to use
Serif
Sans Serif

```html
<!DOCTYPE html>
<html lang="en">
<head>
<meta charset="utf-8">
<title>The Spine Works Chiropractic LLC – Copper Ridge Gym Poster</title>
<link rel="stylesheet" href="https://fonts.googleapis.com/css2?family=Noto+Serif:wght@500&family=Oswald:wght@400&family=Arimo:wght@400&display=swap">
<style>
  :root {
    --orange: #f26a21;
    --navy: #1f2f4d;
    --ink: #2a2a2e;
    --black: #000000;
    --photo-dark: #141518;
    --photo-mid: #34373d;
    --photo-floor: #2a2b2f;
    --photo-shirt: #8a3b33;
    --photo-skin: #7a4e38;
    --photo-steel: #6f737a;
    --silver: #c4c4c4;
  }
  * { margin: 0; padding: 0; box-sizing: border-box; }
  html, body {
    width: 1200px;
    height: 2400px;
    overflow: hidden;
    background: var(--black);
  }
  .poster {
    position: relative;
    width: 1200px;
    height: 2400px;
    overflow: hidden;
  }

  /* Header band */
  .brand-band {
    position: absolute;
    left: 0; top: 0;
    width: 1200px; height: 424px;
    background: var(--orange);
  }
  .brand-mark {
    position: absolute;
    left: 136px; top: 40px;
  }
  .brand-name {
    position: absolute;
    left: 476px; top: 66px;
    font-family: "Noto Serif", Georgia, serif;
    font-weight: 500;
    color: var(--navy);
    line-height: 1;
  }
  .brand-name .line { display: block; }
  .brand-name .line-article { font-size: 42px; margin-bottom: 24px; }
  .brand-name .line-main { font-size: 78px; margin-bottom: 22px; }
  .brand-name .line-sub { font-size: 60px; margin-bottom: 22px; }
  .brand-name .line-web { font-size: 58px; }

  /* Photo area */
  .training-photo {
    position: absolute;
    left: 0; top: 424px;
    width: 1200px; height: 1586px;
    background:
      radial-gradient(ellipse 18% 12% at 48% 15%, var(--photo-dark) 0%, transparent 100%),
      radial-gradient(ellipse 40% 22% at 18% 45%, var(--photo-shirt) 0%, transparent 80%),
      radial-gradient(ellipse 16% 20% at 62% 72%, var(--photo-skin) 0%, transparent 80%),
      radial-gradient(ellipse 60% 10% at 30% 62%, var(--photo-steel) 0%, transparent 80%),
      linear-gradient(180deg, var(--photo-dark) 0%, var(--photo-mid) 30%, var(--photo-floor) 65%, var(--photo-dark) 100%);
  }

  /* Headline word boxes */
  .headline { position: absolute; left: 0; top: 0; width: 1200px; height: 2400px; pointer-events: none; }
  .word {
    position: absolute;
    height: 118px;
    padding: 0 10px;
    background: var(--orange);
    display: flex;
    align-items: center;
    justify-content: space-evenly;
    font-family: "Oswald", "Arial Narrow", sans-serif;
    font-weight: 400;
    font-size: 90px;
    color: var(--ink);
    text-transform: uppercase;
    line-height: 1;
  }
  .word span { display: block; }

  /* Bottom band */
  .tagline-band {
    position: absolute;
    left: 0; top: 2010px;
    width: 1200px; height: 390px;
    background: var(--black);
  }
  .athlete-figure {
    position: absolute;
    left: 0; top: 0;
    width: 1200px; height: 390px;
    background:
      radial-gradient(ellipse 46% 22% at 50% 86%, var(--orange) 0%, rgba(242,106,33,0.5) 50%, transparent 80%),
      radial-gradient(ellipse 9% 22% at 50% 28%, #3a3a3a 0%, transparent 100%),
      var(--black);
  }
  .tagline {
    position: absolute;
    left: 0; top: 248px;
    width: 1200px;
    text-align: center;
    font-family: "Arimo", Arial, sans-serif;
    font-size: 84px;
    color: var(--silver);
    line-height: 1;
  }
</style>
</head>
<body>
<main class="poster">

  <header class="brand-band">
    <svg class="brand-mark" width="268" height="268" viewBox="0 0 268 268" aria-hidden="true">
      <circle cx="134" cy="134" r="124" fill="none" stroke="var(--navy)" stroke-width="10"/>
    </svg>
    <h1 class="brand-name">
      <span class="line line-article">The</span>
      <span class="line line-main">Spine Works</span>
      <span class="line line-sub">Chiropractic LLC</span>
      <span class="line line-web">Alignworks.com</span>
    </h1>
  </header>

  <div class="training-photo" role="img" aria-label="Athlete lying on a weight bench pressing a loaded barbell in a gym"></div>

  <h2 class="headline" aria-label="We specialize in correcting the source of your pain">
    <span class="word" style="left:60px; top:940px; width:180px;" aria-hidden="true"><span>W</span><span>E</span></span>
    <span class="word" style="left:250px; top:940px; width:740px;" aria-hidden="true"><span>S</span><span>P</span><span>E</span><span>C</span><span>I</span><span>A</span><span>L</span><span>I</span><span>Z</span><span>E</span></span>
    <span class="word" style="left:1030px; top:940px; width:140px;" aria-hidden="true"><span>I</span><span>N</span></span>

    <span class="word" style="left:180px; top:1150px; width:740px;" aria-hidden="true"><span>C</span><span>O</span><span>R</span><span>R</span><span>E</span><span>C</span><span>T</span><span>I</span><span>N</span><span>G</span></span>
    <span class="word" style="left:956px; top:1150px; width:214px;" aria-hidden="true"><span>T</span><span>H</span><span>E</span></span>

    <span class="word" style="left:210px; top:1350px; width:440px;" aria-hidden="true"><span>S</span><span>O</span><span>U</span><span>R</span><span>C</span><span>E</span></span>
    <span class="word" style="left:690px; top:1350px; width:130px;" aria-hidden="true"><span>O</span><span>F</span></span>
    <span class="word" style="left:880px; top:1350px; width:290px;" aria-hidden="true"><span>Y</span><span>O</span><span>U</span><span>R</span></span>

    <span class="word" style="left:880px; top:1550px; width:290px;" aria-hidden="true"><span>P</span><span>A</span><span>I</span><span>N</span></span>
  </h2>

  <footer class="tagline-band">
    <div class="athlete-figure" role="img" aria-label="Muscular back silhouette of an athlete with arms outstretched, lit in orange"></div>
    <p class="tagline">Complete Spinal Health</p>
  </footer>

</main>
</body>
</html>
```